K&T Fixit and Rebuild general contracting business card design

I already have a logo that I want to use and I need a card that uses that logo and color scheme on the front with the address phone numbers and email and on the back a place for technicians to write in their name and phone number when they hand it out. It will need the License number of License #KTFXTRB318QN.
It should say General Contractor under the company name. The address is
4417 NE 3rd Ave, Ste D246
Vancouver, WA 98612
www.kandtfixitandrebuild.example
office@kandtfixitandrebuild.example
360-555-0182 is the telephone number
360-555-0149 is the fax number

Target Market(s)

Homeowners needing remodel work or repairs in their home.

Industry/Entity Type

Construction

Contact Information for Business Card

Business name, address, phone number, license number, fax number, email, and website on the front and a place to fill in technician's name and number

Font styles to use
Serif

Requirements
Must have
• Business name, address, phone number, license number, fax number, email, and website on the front and a place to fill in technician's name and number
Nice to have
• I uploaded an example of a front that is good.
Should not have
• Froo froo or extra embellishments.

```html
<!DOCTYPE html>
<html lang="en">
<head>
<meta charset="utf-8">
<title>K&amp;T Fixit and Rebuild — Business Card</title>
<link href="https://fonts.googleapis.com/css2?family=Source+Serif+4:opsz,wght@8..60,400;8..60,700&display=swap" rel="stylesheet">
<style>
  :root {
    --backdrop: #b5b5b5;
    --card-white: #ffffff;
    --brand-red: #a31c21;
    --brand-red-deep: #7e1216;
    --copper: #b5714a;
    --text-gray: #5a5a5a;
    --write-line: #e8b9bb;
  }
  * { margin: 0; padding: 0; box-sizing: border-box; }
  html, body { width: 1200px; height: 1080px; overflow: hidden; }
  body {
    background: var(--backdrop);
    font-family: "Source Serif 4", Georgia, serif;
    position: relative;
  }
  .card {
    position: absolute;
    left: 275px;
    width: 650px;
    height: 371px;
    overflow: hidden;
  }
  .card-front { top: 134px; background: var(--card-white); }
  .card-back { top: 574px; background: var(--brand-red); }

  /* Front */
  .front-brand {
    position: absolute;
    left: 52px; top: 112px;
    width: 255px;
    display: flex; align-items: flex-start; gap: 10px;
  }
  .brand-square {
    width: 20px; height: 20px; flex: none;
    margin-top: 7px;
    background: var(--copper);
  }
  .brand-name {
    font-weight: 700;
    font-size: 26px;
    line-height: 1.12;
    color: var(--copper);
  }
  .brand-tagline {
    margin-top: 6px;
    font-size: 14px;
    letter-spacing: 0.12em;
    text-transform: uppercase;
    color: var(--text-gray);
  }
  .divider {
    position: absolute;
    left: 325px; top: 94px;
    width: 1.5px; height: 186px;
    background: var(--copper);
  }
  .contact {
    position: absolute;
    left: 345px; top: 88px;
    width: 290px;
    color: var(--text-gray);
  }
  .person-name {
    font-weight: 700; font-size: 20px;
    color: var(--brand-red);
    line-height: 1.2;
  }
  .person-title { font-size: 15px; line-height: 1.3; margin-bottom: 16px; }
  .address { font-size: 15px; line-height: 21px; margin-bottom: 10px; padding-left: 2px; }
  .contact-list { list-style: none; font-size: 13.5px; line-height: 20px; }
  .contact-list li { display: flex; align-items: center; gap: 6px; white-space: nowrap; }
  .contact-list svg { width: 11px; height: 11px; flex: none; fill: var(--brand-red); }
  .license-band {
    position: absolute;
    left: 0; top: 324px;
    width: 100%; height: 27px;
    background: var(--brand-red);
    color: var(--card-white);
    font-size: 14.5px;
    text-align: center;
    line-height: 27px;
  }

  /* Back */
  .back-brand {
    position: absolute;
    left: 0; top: 58px; width: 100%;
    text-align: center;
  }
  .back-brand .brand-name {
    color: var(--brand-red-deep);
    font-size: 40px;
    line-height: 1.1;
  }
  .back-brand .brand-tagline {
    color: var(--card-white);
    margin-top: 8px;
  }
  .tech-fields {
    position: absolute;
    left: 95px; top: 218px;
    width: 460px;
  }
  .tech-field {
    display: flex; align-items: flex-end; gap: 12px;
    margin-bottom: 30px;
    color: var(--card-white);
    font-size: 16px;
  }
  .tech-label { width: 95px; flex: none; }
  .tech-line {
    flex: 1;
    height: 1px;
    margin-bottom: 4px;
    background: var(--write-line);
  }
</style>
</head>
<body>
  <section class="card card-front">
    <div class="front-brand">
      <span class="brand-square"></span>
      <div>
        <p class="brand-name">K&amp;T Fixit and Rebuild</p>
        <p class="brand-tagline">General Contractor</p>
      </div>
    </div>
    <div class="divider"></div>
    <div class="contact">
      <p class="person-name">DANIEL WHITAKER</p>
      <p class="person-title">Founder &amp; CEO</p>
      <p class="address">4417 NE 3rd Ave, Ste D246<br>Vancouver, WA 98612</p>
      <ul class="contact-list">
        <li><svg viewBox="0 0 24 24"><path d="M6.6 10.8a15 15 0 0 0 6.6 6.6l2.2-2.2a1 1 0 0 1 1-.25 11.4 11.4 0 0 0 3.6.6 1 1 0 0 1 1 1V20a1 1 0 0 1-1 1A17 17 0 0 1 3 4a1 1 0 0 1 1-1h3.5a1 1 0 0 1 1 1c0 1.25.2 2.45.6 3.6a1 1 0 0 1-.25 1z"/></svg>360-555-0182</li>
        <li><svg viewBox="0 0 24 24"><path d="M6 2h12v6H6zM3 9h18a1 1 0 0 1 1 1v7h-4v5H6v-5H2v-7a1 1 0 0 1 1-1zm5 8v3h8v-3z"/></svg>360-555-0149</li>
        <li><svg viewBox="0 0 24 24"><path d="M2 5h20v14H2zm2 2v.5l8 5.5 8-5.5V7z"/></svg>office@kandtfixitandrebuild.example</li>
        <li><svg viewBox="0 0 24 24"><path d="M12 2a10 10 0 1 0 0 20 10 10 0 0 0 0-20zm0 2c.9 1.2 1.6 2.6 2 4h-4c.4-1.4 1.1-2.8 2-4zM4.3 14a8 8 0 0 1 0-4h3.4a16 16 0 0 0 0 4zm.9 2h3c.3 1.3.8 2.5 1.5 3.6A8 8 0 0 1 5.2 16zM8.2 8h-3a8 8 0 0 1 4.5-3.6A13 13 0 0 0 8.2 8zM12 20c-.9-1.2-1.6-2.6-2-4h4c-.4 1.4-1.1 2.8-2 4zm2.3-6H9.7a14 14 0 0 1 0-4h4.6a14 14 0 0 1 0 4zm.1 5.6c.7-1.1 1.2-2.3 1.5-3.6h3a8 8 0 0 1-4.5 3.6zm1.9-5.6a16 16 0 0 0 0-4h3.4a8 8 0 0 1 0 4z"/></svg>www.kandtfixitandrebuild.example</li>
      </ul>
    </div>
    <div class="license-band">License #KTFXTRB318QN.</div>
  </section>

  <section class="card card-back">
    <div class="back-brand">
      <p class="brand-name">K&amp;T Fixit and Rebuild</p>
      <p class="brand-tagline">General Contractor</p>
    </div>
    <div class="tech-fields">
      <div class="tech-field"><span class="tech-label">Technician</span><span class="tech-line"></span></div>
      <div class="tech-field"><span class="tech-label">Phone</span><span class="tech-line"></span></div>
    </div>
  </section>
</body>
</html>
```